Flyer-Design für Physiotherapie-Praxis
Zielgruppe
Wir sind eine Praxis für Physiotherapie und möchten durch diesen Flyer neue Patienten werben. Der Flyer soll in Arztpraxen ausliegen und dort den Patienten direkt ansprechen und auf uns aufmerksam machen. Es ist auch eine Verknüpfung der Therapie mit einem Training in einem Gesundheitsstudio möglich, da im gleichen Haus das Physio Kraftwerk Eichenstetten beheimatet ist.
Aufgabenstellung
Der Fokus auf unsere Prinzipien (Ganzheitliche Therapie, hohes Maß an Therapiemöglichkeiten, Variation in den therapeutischen Ansätzen durch unterschiedlich fortgebildete Therapeuten, die nach den gleichen Idealen arbeiten)

```html
<!DOCTYPE html>
<html lang="de">
<head>
<meta charset="utf-8">
<title>Flyer – Zentrum für Therapie &amp; Training</title>
<link href="https://fonts.googleapis.com/css2?family=Fira+Sans:wght@400;500;600&display=swap" rel="stylesheet">
<style>
  :root{
    --stage:#00a89f;
    --navy:#333a6e;
    --bar-start:#6cbfa8;
    --bar-end:#1c4b9a;
    --sky-light:#e6f3f8;
    --sky:#7fc3df;
    --aqua-text:#56b6e0;
    --white:#ffffff;
    --logo-blue:#3d86c6;
  }
  *{margin:0;padding:0;box-sizing:border-box}
  html,body{width:1200px;height:675px;overflow:hidden;background:var(--stage);font-family:"Fira Sans",sans-serif}
  .spread{position:absolute;width:577px;height:411px;overflow:hidden}
  .spread--cover{left:31px;top:40px;background:linear-gradient(180deg,var(--sky-light),var(--sky))}
  .spread--inside{left:594px;top:177px;background:linear-gradient(160deg,#cfe8f3,var(--sky))}
  .top-bar{position:absolute;left:0;top:0;width:100%;height:28px;background:linear-gradient(90deg,var(--bar-start),var(--bar-end))}
  .photo-pool{position:absolute;left:189px;top:27px;width:388px;height:265px;background:linear-gradient(180deg,#6f8f66 0%,#8aa36d 35%,#3f86b5 55%,#2b6e9c 100%)}
  .cover-band{position:absolute;left:0;top:107px;width:100%;height:61px;background:rgba(44,110,140,.72)}
  .cover-band__left{position:absolute;left:0;top:0;width:189px;height:100%;background:rgba(120,190,200,.55)}
  .contact-label{position:absolute;left:43px;top:21px;color:var(--white);font-size:15px;font-weight:500}
  .cover-headline{position:absolute;right:20px;top:18px;color:var(--white);font-size:13.5px;font-weight:600;line-height:15px;text-align:center}
  .cover-wave{position:absolute;left:0;top:0}
  .brand{position:absolute;left:400px;top:340px;width:160px;text-align:center;color:var(--logo-blue)}
  .brand__mark{width:22px;height:22px;border-radius:50%;border:1.5px solid var(--logo-blue);margin:0 auto 8px}
  .brand__name{font-size:8px;font-weight:400;line-height:10px;text-transform:uppercase}
  .brand__owner{font-size:7px;margin-top:3px}
  .inside-shape{position:absolute;left:0;top:0}
  .divider{position:absolute;top:27px;width:1px;height:378px;background:rgba(255,255,255,.35)}
  .intro{position:absolute;left:27px;top:42px;width:140px;color:var(--white);font-size:8.6px;line-height:11.3px;font-weight:500}
  .intro-more{position:absolute;left:29px;top:166px;width:150px;color:var(--white);font-size:7.3px;line-height:10px}
  .photo-team{position:absolute;left:30px;top:285px;width:151px;height:110px;border:4px solid var(--white);border-radius:6px;background:linear-gradient(180deg,#4a5570,#8fc3dc 60%,#5b8fae)}
  .section-title{position:absolute;left:205px;top:50px;width:280px;text-align:center;color:var(--white);font-size:12px;font-weight:500}
  .section-text{position:absolute;left:205px;top:75px;width:280px;text-align:center;color:var(--white);font-size:7px;line-height:10.1px}
  .training-title{position:absolute;left:200px;top:168px;width:184px;text-align:center;color:var(--aqua-text);font-size:11px;line-height:10px;font-weight:500}
  .training-text{position:absolute;left:200px;top:211px;width:184px;text-align:center;color:var(--aqua-text);font-size:7px;line-height:10.1px;font-weight:500}
  .hex-photos{position:absolute;left:0;top:0}
</style>
</head>
<body>

<section class="spread spread--cover">
  <div class="top-bar"></div>
  <div class="photo-pool" role="img" aria-label="Foto: Bewegungsbad im Wintergarten mit Pflanzen und Schwimmnudeln"></div>
  <div class="cover-band">
    <div class="cover-band__left"></div>
    <p class="contact-label">Contact info</p>
    <h1 class="cover-headline">WIR SIND THERAPEUTEN<br>AUS ÜBERZEUGUNG!</h1>
  </div>
  <svg class="cover-wave" width="577" height="411" viewBox="0 0 577 411">
    <path d="M0 330 C120 280 260 268 340 275 C440 283 520 290 577 292 L577 411 L0 411 Z" fill="var(--bar-start)" opacity=".85"/>
    <path d="M0 345 C110 290 250 277 340 282 C440 288 520 296 577 298 L577 411 L0 411 Z" fill="var(--logo-blue)"/>
    <path d="M0 352 C110 300 250 285 340 290 C440 295 520 303 577 305 L577 411 L0 411 Z" fill="var(--navy)"/>
  </svg>
  <div class="brand">
    <div class="brand__mark"></div>
    <p class="brand__name">Zentrum für Therapie &amp; Training<br>Lorenz Adler &amp; Sabine Kurtz</p>
    <p class="brand__owner">Inhaberin: Sabine Kurtz</p>
  </div>
</section>

<section class="spread spread--inside">
  <svg class="inside-shape" width="577" height="411" viewBox="0 0 577 411">
    <path d="M0 27 H466 L560 128 Q572 145 562 165 L353 411 H0 Z" fill="var(--navy)"/>
  </svg>
  <div class="top-bar"></div>
  <div class="divider" style="left:196px"></div>
  <div class="divider" style="left:386px"></div>

  <p class="intro">Unsere Praxis gibt es seit 1969. In dieser Zeit konnten wir viel Erfahrung sammeln. Wir sind ein Team aus älteren und jüngeren Therapeuten, aus Masseuren, med. Bademeistern und Physiotherapeuten. Diese bunte Mischung beinhaltet viel Erfahrung und viel Wissen.</p>
  <p class="intro-more">Beides wird in regelmäßigen internen Fortbildungen ausgetauscht. So ergänzen wir uns gegenseitig. Wir arbeiten als Team Hand in Hand und schätzen das Fachwissen jedes einzelnen Kollegen.<br>Wir sind motiviert und mit Freude bei der Arbeit, denn wir wissen, was unsere Patienten mit Hilfe der Physiotherapie erreichen können.</p>
  <div class="photo-team" role="img" aria-label="Gruppenfoto des Praxisteams in hellblauen Poloshirts"></div>

  <h2 class="section-title">Vielzahl von Therapiemöglichkeiten</h2>
  <p class="section-text">Wir haben eine Vielzahl von Therapiegeräten und -hilfsmitteln zur Verfügung, z.B. eine Kletterwand, Sling Trainer, eine Vibrano®-Rüttelplatte, ein Slack Rack und ein Bewegungsbad! Im 32°C warmem Wasser können sich unsere Patienten besser bewegen. Mit unserem Fachwissen und unserer Erfahrung haben wir uns auf die Behandlung orthopädischer, chirurgischer und neurologischer Patienten spezialisiert.</p>

  <h3 class="training-title">AKTIVES<br>GesundheitsTRAINING</h3>
  <p class="training-text">Für gute Fortschritte in der Therapie und die Erhaltung dieser Fortschritte ist der Weg zur sportlichen Aktivität essentiell. Diesen Weg erleichtern wir unseren Patienten durch unser Angebot des Aktiven Gesundheitstrainings. Zusätzlich zu Ihrem Rezept erhalten unsere neuen Patienten einen zusätzlichen und kostenfreien Beratungstermin im Physio Kraftwerk Eichenstetten. In diesem Termin zeigen wir Ihnen Möglichkeiten, selbst etwas zu Ihrer Gesundheit beizutragen.<br>Je nachdem, was Ihnen gerade am effektivsten hilft, trainieren Sie 6 x am Kraft-Ausdauer-Zirkel der Firma Fortima oder am Kinetra-Zirkel. Das Training an diesen Geräten ist einfach, sicher und effektiv. Da das Training maximal 35 Minuten Zeit beansprucht ist Zeitmangel kein Argument mehr</p>

  <svg class="hex-photos" width="577" height="411" viewBox="0 0 577 411">
    <defs>
      <linearGradient id="gymTone" x1="0" y1="0" x2="0" y2="1">
        <stop offset="0" stop-color="#cfd6d2"/><stop offset="1" stop-color="#8c9496"/>
      </linearGradient>
      <linearGradient id="roomTone" x1="0" y1="0" x2="1" y2="1">
        <stop offset="0" stop-color="#e8dca8"/><stop offset="1" stop-color="#b3a58a"/>
      </linearGradient>
    </defs>
    <polygon role="img" aria-label="Foto: Trainingsraum mit Kraftgeräten" points="402,201 434,146 496,146 528,201 496,256 434,256" fill="url(#gymTone)" stroke="var(--white)" stroke-width="3" stroke-linejoin="round"/>
    <polygon role="img" aria-label="Foto: Behandlungsraum mit Therapieliege" points="419,331 452,273 518,273 551,331 518,389 452,389" fill="url(#roomTone)" stroke="var(--white)" stroke-width="3" stroke-linejoin="round"/>
  </svg>
</section>

</body>
</html>
```